Finiding oppertunites in Real Estate 6.15.20

size of ad 7” x 9.6”
1-I like the ad to stand out and attract people's attention.
2-you should be able to see the text of the ad clearly .. see the attachment anything in yellow is instructions.
3-the list of topics should not be the main part of the ad
4-if you decide you want a picture or vector of a person .. (you decide)
then it should be a white male about 25-30 years old wearing a solid white or blue shirt and not long hair.
5-leave 1 inch for footer
see attachment
Good luck

Target Market(s)

potential male students 25-35 years of age

Industry/Entity Type

Education

Requirements
Must have
• will stand out and people would want to see it.
should be able to read the words of ad
Nice to have
• how to make money in real estate on one line

```html
<!DOCTYPE html>
<html lang="en">
<head>
<meta charset="utf-8">
<title>Real Estate Career Course</title>
<link href="https://fonts.googleapis.com/css2?family=Barlow:wght@300;400;500;600;700&display=swap" rel="stylesheet">
<style>
  :root {
    --ink: #141414;
    --ink-soft: #3a3a3a;
    --white: #ffffff;
    --gold: #e8c46c;
    --panel-dark: #2b1d11;
    --panel-mid: #6b4a26;
    --photo-light: #e6e9ec;
    --photo-mid: #b9c0c7;
    --rule: #9a9a9a;
    --red-light: #e0454a;
    --red-deep: #8e0c12;
    --paper: #f6f6f6;
  }
  * { margin: 0; padding: 0; box-sizing: border-box; }
  html, body { width: 875px; height: 1200px; overflow: hidden; }
  body { font-family: "Barlow", sans-serif; color: var(--ink); background: var(--paper); }
  .ad { position: relative; width: 875px; height: 1200px; overflow: hidden; background: linear-gradient(180deg, #fbfbfb 0%, #f1f1f1 100%); }

  .hero { position: absolute; left: 0; top: 0; width: 875px; height: 675px; }
  .hero-photo { position: absolute; inset: 0; background: linear-gradient(160deg, var(--photo-light) 0%, #cfd4da 45%, var(--photo-mid) 100%); }
  .hero-panel { position: absolute; left: 0; top: 0; width: 875px; height: 675px; }

  .headline { position: absolute; left: 98px; top: 0; color: var(--white); }
  .headline .line { position: absolute; left: 0; white-space: nowrap; font-weight: 600; }
  .title-main { top: 112px; font-size: 60px; letter-spacing: 1.5px; }
  .title-sub { top: 180px; font-size: 60px; letter-spacing: 2.2px; color: var(--gold); }
  .hook-lead { top: 302px; font-size: 47px; letter-spacing: 2.8px; }
  .hook-money { top: 343px; font-size: 94px; font-weight: 700; line-height: 1; letter-spacing: 5px; }
  .hook-tail { top: 435px; font-size: 33px; letter-spacing: 1.4px; color: var(--gold); }

  .intro { position: absolute; left: 94px; top: 702px; width: 440px; }
  .intro-lead { font-size: 26px; font-weight: 500; line-height: 31px; letter-spacing: 0.3px; }
  .intro-note { margin-top: 10px; font-size: 23px; font-weight: 300; line-height: 30px; color: var(--ink-soft); letter-spacing: 0.7px; }

  .badge { position: absolute; left: 44px; top: 846px; width: 412px; height: 112px; }
  .badge-label { position: absolute; left: 44px; top: 846px; width: 412px; height: 112px; display: flex; align-items: center; justify-content: center; color: var(--white); font-size: 29px; font-weight: 600; letter-spacing: 0.6px; }

  .schedule { position: absolute; left: 94px; top: 970px; font-size: 26px; font-weight: 500; line-height: 32px; letter-spacing: 0.5px; }

  .topics { position: absolute; left: 543px; top: 675px; width: 340px; height: 384px; border-left: 1px solid var(--rule); border-bottom: 1px solid var(--rule); border-bottom-left-radius: 6px; padding: 34px 0 0 34px; }
  .topics-title { font-size: 20px; font-weight: 500; letter-spacing: 0.4px; margin-bottom: 10px; }
  .topics-list { list-style: none; font-size: 16.5px; font-weight: 300; line-height: 21px; letter-spacing: 0.5px; color: var(--ink-soft); }
</style>
</head>
<body>
<div class="ad">
  <section class="hero">
    <div class="hero-photo" role="img" aria-label="Photo of a smiling young businessman in a white shirt and blue tie, arms crossed, leaning in a bright office doorway"></div>
    <svg class="hero-panel" viewBox="0 0 875 675" role="img" aria-label="Warm blurred office interior behind the headline">
      <defs>
        <linearGradient id="panelTone" x1="0" y1="0" x2="0.6" y2="1">
          <stop offset="0" stop-color="#8a6338"/>
          <stop offset="0.45" stop-color="#6b4a26"/>
          <stop offset="1" stop-color="#2b1d11"/>
        </linearGradient>
      </defs>
      <polygon points="0,0 605,0 277,675 0,675" fill="url(#panelTone)"/>
    </svg>

    <div class="headline">
      <div class="line title-main">Real Estate</div>
      <div class="line title-sub">Career Course</div>
      <div class="line hook-lead">How to Make</div>
      <div class="line hook-money">Money</div>
      <div class="line hook-tail">In Real Estate?</div>
    </div>
  </section>

  <div class="intro">
    <p class="intro-lead">For those who have started<br>or would like to go into Real Estate</p>
    <p class="intro-note">An investment in knowledge<br>opens up untold opportunities</p>
  </div>

  <svg class="badge" viewBox="0 0 410 112" aria-hidden="true">
    <defs>
      <linearGradient id="burstTone" x1="0" y1="0" x2="0" y2="1">
        <stop offset="0" stop-color="#e0454a"/>
        <stop offset="1" stop-color="#8e0c12"/>
      </linearGradient>
    </defs>
    <polygon fill="url(#burstTone)" points="408,56 371,62 398,73 355,74 369,88 324,84 324,100 281,92 268,108 231,96 205,111 179,96 142,108 129,92 86,100 86,84 41,88 55,74 12,73 39,62 2,56 39,50 12,39 55,38 41,24 86,28 86,12 129,20 142,4 179,16 205,1 231,16 268,4 281,20 324,12 324,28 369,24 355,38 398,39 371,50"/>
    <ellipse cx="205" cy="44" rx="148" ry="26" fill="#ffffff" opacity="0.18"/>
  </svg>
  <div class="badge-label">Remote sessions</div>

  <p class="schedule">12 Session Course<br>Classes starting June 16</p>

  <aside class="topics">
    <h2 class="topics-title">A Partial listing of Topics</h2>
    <ul class="topics-list">
      <li>Single-family</li>
      <li>Multifamily</li>
      <li>Management</li>
      <li>Real Estate Concepts</li>
      <li>Real Estate law</li>
      <li>Investment properties</li>
      <li>Foreclosures</li>
      <li>Rehab</li>
      <li>Foreclosures</li>
      <li>Short sales</li>
      <li>Development</li>
      <li>Finical modeling</li>
      <li>HUD properties</li>
      <li>Due Diligence</li>
    </ul>
  </aside>
</div>
</body>
</html>
```